Note/Card sent to show appreciation to partners who worked with us to improve local communities

I'd like a simple note/card designed for a wide audience. Originally, I called this a "Thanksgiving Card," but it's really just a card to be sent around Thanksgiving, not specifically celebrating the Thanksgiving holiday. We plan to send the card out just prior to Thanksgiving 2017 (Nov. 24, 2017). I work at a regulated electric utility, and we'd like to say thank you to the many stakeholders who we partner with throughout the year to support initiatives that help to improve our state and create opportunities for economic growth. I'm interested mostly in the design of the card, not the simple verbiage on the inside.
Customers, charitable foundations, nonprofits, advocacy groups, industry associations, friends

```html
<!DOCTYPE html>
<html lang="en">
<head>
<meta charset="utf-8">
<title>Thank You Card</title>
<link href="https://fonts.googleapis.com/css2?family=Nunito+Sans:wght@600;800&display=swap" rel="stylesheet">
<style>
  :root {
    --page-bg: #eef0f3;
    --card-white: #ffffff;
    --ink-navy: #1b1f5c;
    --blue-light: #45aee9;
    --blue-mid: #1c86d6;
    --blue-deep: #0b56ac;
  }
  html, body {
    margin: 0;
    padding: 0;
    width: 1200px;
    height: 750px;
    overflow: hidden;
    background: var(--page-bg);
  }
  .canvas {
    position: relative;
    width: 1200px;
    height: 750px;
  }
  .card {
    position: absolute;
    left: 100px;
    top: 17px;
    width: 1000px;
    height: 716px;
    background: var(--card-white);
    overflow: hidden;
    box-shadow: 0 2px 10px rgba(0, 0, 0, 0.12);
  }
  .card-wave {
    position: absolute;
    inset: 0;
    width: 100%;
    height: 100%;
  }
  .card-message {
    position: absolute;
    left: 38px;
    top: 255px;
    font-family: "Nunito Sans", sans-serif;
    color: var(--ink-navy);
  }
  .card-title {
    margin: 0;
    font-size: 112px;
    font-weight: 800;
    line-height: 1;
    letter-spacing: -1px;
  }
  .card-subtitle {
    margin: 6px 0 0 2px;
    font-size: 44px;
    font-weight: 600;
    line-height: 1.1;
  }
</style>
</head>
<body>
  <main class="canvas">
    <section class="card">
      <svg class="card-wave" viewBox="0 0 1000 716" role="img" aria-label="Blue swooping wave with halftone dots framing a white oval area" preserveAspectRatio="none">
        <defs>
          <linearGradient id="wave-fill" x1="0" y1="0" x2="1" y2="1">
            <stop offset="0" stop-color="var(--blue-mid)"/>
            <stop offset="0.6" stop-color="var(--blue-light)"/>
            <stop offset="1" stop-color="var(--blue-mid)"/>
          </linearGradient>
          <radialGradient id="white-glow" cx="0.5" cy="0.5" r="0.5">
            <stop offset="0" stop-color="#ffffff"/>
            <stop offset="0.86" stop-color="#ffffff"/>
            <stop offset="1" stop-color="#ffffff" stop-opacity="0"/>
          </radialGradient>
          <filter id="band-blur" x="-20%" y="-20%" width="140%" height="140%">
            <feGaussianBlur stdDeviation="22"/>
          </filter>
        </defs>
        <rect class="wave-base" width="1000" height="716" fill="url(#wave-fill)"/>
        <ellipse class="wave-band" cx="300" cy="380" rx="560" ry="600" fill="none" stroke="var(--blue-deep)" stroke-width="70" opacity="0.75" filter="url(#band-blur)"/>
        <ellipse class="white-oval" cx="290" cy="380" rx="600" ry="640" fill="url(#white-glow)"/>
      </svg>
      <div class="card-message">
        <h1 class="card-title">Thank You</h1>
        <p class="card-subtitle">For The Amazing Support</p>
      </div>
    </section>
  </main>
</body>
</html>
```